Brightwell cleaning and maintenance company

An expansive website whereby we can advertise our commercial cleaning and maintenance services across a service portfolio of commercial cleaning and property maintenance. Whereby potential skilled resources can deposit there resume so we can collaborate and match candidates to a broad range of cleaning and maintenance jobs/projects.
Updates

Looking for more extensive ideas so the front page can change pictures on it with the focus for Brightwell Commercial Cleaning and Maintenance. Also need to bring in all the portfolios we offer including 1. Equipment Cleaning and Sanitisation Services 2. High pressure gurney and play ground equipment cleaning 3. General Cleaning and Property Facilities Management 4. Project and Recruiting Services, to allow for potential professional cleaners, handy man, mechanics, warehousing resources , electricians to deposit there resume. Most of the designers have stuck with the old portfolio categories , however the portfolio of services we offer has been updated so that needs to be reflected in the website. Also not necessary to use all my original photos I would like the opening page of the website to perhaps be able to change and have different pictures is that possible thank you

```html
<!DOCTYPE html>
<html lang="en">
<head>
<meta charset="utf-8">
<title>Brightwell — Commercial Cleaning &amp; Maintenance</title>
<link rel="stylesheet" href="https://fonts.googleapis.com/css2?family=Noto+Serif:wght@400;700&family=Poppins:wght@400;500;600&display=swap">
<style>
:root{
  --orange:#f0521a;
  --navy:#1f3f6e;
  --text:#666;
  --muted:#888;
  --light:#f3f3f3;
  --white:#fff;
}
*{margin:0;padding:0;box-sizing:border-box}
html,body{width:1200px;height:5249px;overflow:hidden}
body{position:relative;background:var(--white);font-family:"Poppins",sans-serif;color:var(--text)}
.abs{position:absolute}
.btn{position:absolute;background:var(--orange);color:#fff;border-radius:30px;font-family:"Noto Serif",serif;font-weight:700;font-size:16px;display:flex;align-items:center;justify-content:center;letter-spacing:.5px}
.eyebrow{position:absolute;color:var(--orange);font-size:17px}
.h2{position:absolute;font-family:"Noto Serif",serif;color:var(--navy);font-size:40px;line-height:1.2;font-weight:400}
.para{position:absolute;font-size:14px;line-height:25px;color:var(--text)}
.photo{position:absolute}

/* header */
.site-header{position:absolute;left:0;top:0;width:1200px;height:92px;background:#fff;z-index:3}
.brand{position:absolute;left:77px;top:24px;display:flex;align-items:center;gap:10px;font-family:"Noto Serif",serif;font-size:34px;color:var(--orange)}
.brand-dot{width:30px;height:30px;border-radius:50%;background:var(--navy)}
.nav a{position:absolute;top:28px;height:40px;line-height:40px;font-size:14px;color:#222;text-decoration:none}
.nav .active{background:var(--orange);color:#fff;border-radius:22px;width:94px;text-align:center}

/* hero */
.hero-photo{left:0;top:92px;width:1200px;height:620px;background:linear-gradient(180deg,#e9ebec 0%,#d8dadb 55%,#b9bcbd 100%)}
.hero-title{position:absolute;left:0;width:1200px;top:258px;text-align:center;font-family:"Noto Serif",serif;font-weight:700;font-size:62px;letter-spacing:1px;line-height:80px}
.hero-title .o{color:var(--orange)}.hero-title .n{color:var(--navy)}
.hero-sub{position:absolute;left:0;width:1200px;top:336px;text-align:center;font-size:16px;color:#222}
.phone-pill{position:absolute;left:485px;top:388px;width:233px;height:52px;border-radius:26px;background:var(--navy);color:#fff;font-family:"Noto Serif",serif;font-weight:700;font-size:17px;padding-left:80px;line-height:52px}
.phone-icon{position:absolute;left:480px;top:378px;width:70px;height:70px;border-radius:50%;background:var(--orange);border:5px solid #fff;display:flex;align-items:center;justify-content:center}
.quote-badge{position:absolute;left:840px;top:537px;width:152px;height:152px;border-radius:50%;background:var(--orange);border:5px solid var(--navy);color:#fff;font-family:"Noto Serif",serif;font-weight:700;font-size:22px;line-height:26px;text-align:center;display:flex;align-items:center;justify-content:center;z-index:2}

/* services */
.services-bg{left:0;top:1330px;width:1200px;height:650px;background:linear-gradient(180deg,#fff 0%,#eceeef 50%,#e2e4e5 100%)}
.card{position:absolute;top:1348px;width:234px;height:477px;background:#fff;box-shadow:0 4px 18px rgba(0,0,0,.06)}
.card .photo{left:12px;top:4px;width:210px;height:210px}
.card h3{position:absolute;left:18px;top:240px;width:200px;font-family:"Noto Serif",serif;color:var(--navy);font-size:17px;line-height:25px;font-weight:400}
.card p{position:absolute;left:18px;top:330px;width:200px;font-size:13px;line-height:24px;color:var(--muted)}
.card .more{position:absolute;left:18px;top:430px;font-family:"Noto Serif",serif;font-weight:700;color:var(--orange);font-size:14px}

/* attributes */
.attr{position:absolute;width:280px;text-align:center}
.attr .ico{margin:0 auto;width:72px;height:72px;border:3px solid #222;border-radius:50%;position:relative}
.attr .ico::after{content:"";position:absolute;left:26px;top:26px;width:14px;height:14px;border-radius:50%;background:var(--orange)}
.attr span{display:block;margin-top:22px;font-family:"Noto Serif",serif;color:var(--navy);font-size:19px}

/* portfolio */
.arrow{position:absolute;width:58px;height:58px;border-radius:50%;display:flex;align-items:center;justify-content:center}

/* blog */
.blog-bg{left:0;top:3700px;width:1200px;height:670px;background:var(--light)}
.post{position:absolute;top:3850px;width:324px;height:410px;background:#fff}
.post .photo{left:12px;top:12px;width:300px;height:208px}
.post h3{position:absolute;left:12px;top:240px;font-family:"Noto Serif",serif;color:var(--navy);font-size:15px;line-height:27px;font-weight:700}
.post .date{position:absolute;left:12px;top:300px;font-size:12px;color:var(--orange)}
.post p{position:absolute;left:12px;top:328px;width:300px;font-size:13px;line-height:25px;color:var(--muted)}

/* clients */
.client{position:absolute;top:4622px;height:40px;display:flex;align-items:center;gap:8px;font-family:"Noto Serif",serif;font-weight:700;font-size:20px;color:var(--navy);white-space:nowrap}
.client i{display:block;width:14px;height:14px;background:var(--orange)}

/* footer */
.footer h4{position:absolute;font-family:"Noto Serif",serif;color:#fff;font-size:19px;font-weight:700}
.footer li{list-style:none;position:absolute;font-size:14px;color:#fff}
.footer li::before{content:"";display:inline-block;width:6px;height:6px;border-radius:50%;background:var(--orange);margin-right:14px;vertical-align:middle}
.footer .info{position:absolute;font-size:14px;color:#fff;display:flex;align-items:center;gap:18px}
.social{position:absolute;top:5062px;width:44px;height:44px;border-radius:50%;background:var(--orange);color:#fff;font-weight:600;font-size:16px;display:flex;align-items:center;justify-content:center}
.copyright{position:absolute;left:0;top:5185px;width:1200px;height:64px;background:var(--orange);color:#fff;font-size:13px;text-align:center;line-height:64px}
</style>
</head>
<body>

<header class="site-header">
  <div class="brand"><span class="brand-dot"></span>Brightwell</div>
  <nav class="nav">
    <a class="active" style="left:442px">HOME</a>
    <a style="left:560px">SERVICES</a>
    <a style="left:654px">ABOUT US</a>
    <a style="left:752px">OUR PEOPLE</a>
    <a style="left:860px">SAFETY &amp; COMPLIANCE</a>
    <a style="left:1048px">CONTACT</a>
  </nav>
</header>

<!-- hero -->
<div class="photo hero-photo" role="img" aria-label="Bright modern office interior with desks, chairs and potted plants"></div>
<svg class="abs" style="left:0;top:560px" width="1200" height="160" viewBox="0 0 1200 160" aria-hidden="true">
  <path d="M0 40 C120 150 300 150 420 90 C520 40 560 130 700 130 C820 130 880 40 1000 40 C1100 40 1160 70 1200 90 L1200 160 L0 160Z" fill="#fff"/>
  <path d="M0 40 C120 150 300 150 420 90 C520 40 560 130 700 130 C820 130 880 40 1000 40 C1100 40 1160 70 1200 90" fill="none" stroke="#1f3f6e" stroke-width="6"/>
</svg>
<h1 class="hero-title"><span class="o">CLEANING</span> <span class="n">BRIGHTWELL</span></h1>
<p class="hero-sub">Your Source for Commercial &amp; Food Services Equipment Cleaning.</p>
<div class="phone-pill">(07) 3900 5172</div>
<div class="phone-icon">
  <svg width="26" height="26" viewBox="0 0 24 24"><path d="M6.6 10.8a15 15 0 0 0 6.6 6.6l2.2-2.2a1 1 0 0 1 1-.25 11.4 11.4 0 0 0 3.6.57 1 1 0 0 1 1 1V20a1 1 0 0 1-1 1A17 17 0 0 1 3 4a1 1 0 0 1 1-1h3.5a1 1 0 0 1 1 1c0 1.25.2 2.45.57 3.57a1 1 0 0 1-.25 1z" fill="#fff"/></svg>
</div>
<div class="quote-badge">GET A<br>FREE<br>QUOTE</div>

<!-- welcome -->
<div class="eyebrow" style="left:80px;top:786px">Welcome To</div>
<h2 class="h2" style="left:78px;top:816px;font-size:46px">Brightwell</h2>
<p class="para" style="left:80px;top:884px;width:470px">We are Brightwell, a leading, Australian owned, cleaning services company. When you work with Brightwell it is easy to do business with us.</p>
<p class="para" style="left:80px;top:970px;width:470px">Our people are professional, reliable and service oriented. In every interaction you have; on site, receiving help from our service support staff, or rolling-out new cleaning.</p>
<div class="btn" style="left:77px;top:1064px;width:187px;height:56px">LEARN MORE</div>
<div class="abs" style="left:1030px;top:756px;width:93px;height:374px;background:var(--orange)"></div>
<div class="photo" style="left:658px;top:768px;width:452px;height:352px;background:linear-gradient(135deg,#e4e6e8,#b9c0c6 60%,#6f7c8a)" role="img" aria-label="Two cleaners in uniform vacuuming and wiping an office"></div>

<!-- services -->
<div class="photo services-bg" role="img" aria-label="Soft faded office background"></div>
<div class="eyebrow" style="left:0;width:1200px;text-align:center;top:1222px">What We Do</div>
<h2 class="h2" style="left:0;width:1200px;text-align:center;top:1258px">We Offer Best Cleaning Services</h2>

<article class="card" style="left:102px">
  <div class="photo" style="background:linear-gradient(135deg,#8a8278,#d2cbc2 55%,#6e6a64)" role="img" aria-label="Chef wiping a stainless steel kitchen bench"></div>
  <h3>Equipment Cleaning &amp; Sanitisation Services</h3>
  <p>Full cleaning, sanitising and tune up of food service equipment.</p>
  <span class="more">Read More....</span>
</article>
<article class="card" style="left:356px">
  <div class="photo" style="background:linear-gradient(135deg,#6f7f5a,#c9b56a 50%,#8c8a82)" role="img" aria-label="Worker in protective suit using a high pressure water cleaner"></div>
  <h3>High Pressure Gurney &amp; Playground Cleaning</h3>
  <p>Pressure cleaning for hard surfaces and playground equipment.</p>
  <span class="more">Read More....</span>
</article>
<article class="card" style="left:610px">
  <div class="photo" style="background:linear-gradient(135deg,#e6e9ec,#8fa2b6 55%,#3b4f66)" role="img" aria-label="Cleaner mopping a commercial building floor"></div>
  <h3>General Cleaning &amp; Property Facilities Management</h3>
  <p>Routine cleaning and upkeep of commercial properties and sites.</p>
  <span class="more">Read More....</span>
</article>
<article class="card" style="left:864px">
  <div class="photo" style="background:linear-gradient(135deg,#d9dde2,#9aa6b4 55%,#2f4a6d)" role="img" aria-label="Tradespeople reviewing plans on a work site"></div>
  <h3>Project &amp; Recruiting Services</h3>
  <p>Cleaners, handymen, mechanics, warehousing staff and electricians.</p>
  <span class="more">Read More....</span>
</article>
<div class="btn" style="left:506px;top:1857px;width:187px;height:55px">VIEW MORE</div>

<!-- attributes -->
<h2 class="h2" style="left:0;width:1200px;text-align:center;top:2062px;line-height:48px">Brightwell Service Technician<br>Attributes</h2>
<p class="para" style="left:0;width:1200px;text-align:center;top:2168px">Our people are carefully selected and are recruited from qualified trades backgrounds<br>or with equivalent on the job experience.</p>

<div class="attr" style="left:171px;top:2278px"><div class="ico" role="img" aria-label="Communicator icon"></div><span>Communicators</span></div>
<div class="attr" style="left:460px;top:2278px"><div class="ico" role="img" aria-label="Knowledge icon"></div><span>knowledgeable</span></div>
<div class="attr" style="left:751px;top:2278px"><div class="ico" role="img" aria-label="Team competence icon"></div><span>Technically Competent</span></div>
<div class="attr" style="left:171px;top:2455px"><div class="ico" role="img" aria-label="Respect icon"></div><span>Respectful</span></div>
<div class="attr" style="left:460px;top:2455px"><div class="ico" role="img" aria-label="Ethics icon"></div><span>Ethical</span></div>
<div class="attr" style="left:751px;top:2455px"><div class="ico" role="img" aria-label="Checklist icon"></div><span>Detail Oriented</span></div>

<!-- portfolio -->
<div class="photo" style="left:465px;top:2658px;width:735px;height:457px;background:linear-gradient(180deg,#fafafa,#ececec 70%,#dadada)" role="img" aria-label="Soft grey room backdrop"></div>
<div class="eyebrow" style="left:80px;top:2815px">Our Work</div>
<h2 class="h2" style="left:78px;top:2843px;font-size:46px">Portfolio</h2>
<div class="arrow" style="left:76px;top:2921px;background:var(--orange)"><svg width="18" height="18" viewBox="0 0 24 24"><path d="M15 4l-8 8 8 8" fill="none" stroke="#fff" stroke-width="2.5"/></svg></div>
<div class="arrow" style="left:139px;top:2921px;border:2px solid var(--orange);background:#fff"><svg width="18" height="18" viewBox="0 0 24 24"><path d="M9 4l8 8-8 8" fill="none" stroke="#f0521a" stroke-width="2.5"/></svg></div>
<div class="photo" style="left:344px;top:2777px;width:248px;height:213px;background:linear-gradient(135deg,#f0521a,#f59b6d)" role="img" aria-label="Worker cleaning a table, orange tint"></div>
<div class="photo" style="left:610px;top:2777px;width:247px;height:213px;background:linear-gradient(135deg,#f26a2c,#f28a4e)" role="img" aria-label="Paint roller on an orange surface"></div>
<div class="photo" style="left:876px;top:2777px;width:247px;height:213px;background:linear-gradient(135deg,#5d8fb0,#d7e2ea 60%,#f3f5f6)" role="img" aria-label="Gloved hands spraying and wiping a bench"></div>

<!-- find a job -->
<div class="photo" style="left:0;top:3110px;width:580px;height:590px;border-radius:50%;background:radial-gradient(circle,#f2f4f6 0%,#e3e7ea 55%,#fff 72%)" role="img" aria-label="Top-down view of people meeting in red chairs around a glass table"></div>
<h2 class="h2" style="left:596px;top:3246px">Find A Job</h2>
<p class="para" style="left:597px;top:3306px;width:420px;line-height:28px">Send Your Resume so we can collaborate and match candidates to a broad range of cleaning and maintenance jobs/projects.</p>
<div class="abs" style="left:592px;top:3410px;width:468px;height:52px;border-radius:26px;background:#f1f1f1;font-size:13px;color:#777;line-height:52px;padding-left:28px">Attach You Resume
  <svg class="abs" style="right:18px;top:16px" width="20" height="20" viewBox="0 0 24 24"><path d="M20 11l-8 8a5 5 0 0 1-7-7l9-9a3.5 3.5 0 0 1 5 5l-9 9a2 2 0 0 1-3-3l8-8" fill="none" stroke="#888" stroke-width="1.6"/></svg>
</div>
<div class="btn" style="left:596px;top:3478px;width:145px;height:54px">SUBMIT</div>

<!-- blog -->
<div class="photo blog-bg" role="img" aria-label="Light grey band"></div>
<h2 class="h2" style="left:0;width:1200px;text-align:center;top:3780px">Recent Blog</h2>
<article class="post" style="left:77px">
  <div class="photo" style="background:linear-gradient(135deg,#1f2d3d,#6b7f93 55%,#c7a27a)" role="img" aria-label="Chef cooking in a commercial kitchen"></div>
  <h3>Lorem ipsum is simply dummt text<br>and printing and typesetting.</h3>
  <span class="date">9 April 2020</span>
  <p>Lorem Ipsum is simply dummy text of the printing and typesetting industry...</p>
</article>
<article class="post" style="left:439px">
  <div class="photo" style="background:linear-gradient(135deg,#6a8f3f,#c1d28a 50%,#d9493a)" role="img" aria-label="Children playing on a playground slide"></div>
  <h3>Lorem ipsum is simply dummt text<br>and printing and typesetting.</h3>
  <span class="date">9 April 2020</span>
  <p>Lorem Ipsum is simply dummy text of the printing and typesetting industry...</p>
</article>
<article class="post" style="left:800px">
  <div class="photo" style="background:linear-gradient(135deg,#e8dfd5,#c8a892 55%,#d4607a)" role="img" aria-label="Woman spraying and wiping a kitchen counter"></div>
  <h3>Lorem ipsum is simply dummt text<br>and printing and typesetting.</h3>
  <span class="date">9 April 2020</span>
  <p>Lorem Ipsum is simply dummy text of the printing and typesetting industry...</p>
</article>

<!-- clients -->
<h2 class="h2" style="left:0;width:1200px;text-align:center;top:4456px">Our Clients</h2>
<p class="para" style="left:0;width:1200px;text-align:center;top:4516px">Brightwell has established a strong reputation as being reliable, responsive and<br>dedicated to fulfilling our customers and partners cleaning service needs.</p>
<svg class="abs" style="left:76px;top:4626px" width="20" height="34" viewBox="0 0 20 34"><path d="M16 2L4 17l12 15" fill="none" stroke="#bbb" stroke-width="2"/></svg>
<svg class="abs" style="left:1104px;top:4626px" width="20" height="34" viewBox="0 0 20 34"><path d="M4 2l12 15-12 15" fill="none" stroke="#bbb" stroke-width="2"/></svg>
<div class="client" style="left:130px"><i></i>Ember Grill</div>
<div class="client" style="left:320px"><i></i>Kitchora</div>
<div class="client" style="left:490px"><i></i>Fizzwell Co</div>
<div class="client" style="left:686px"><i></i>Goldarch</div>
<div class="client" style="left:860px"><i></i>R.T. Hallam</div>

<!-- footer -->
<svg class="abs" style="left:0;top:4770px" width="1200" height="420" viewBox="0 0 1200 420" aria-hidden="true">
  <path d="M0 210 C300 60 450 40 600 40 C750 40 900 60 1200 210 L1200 420 L0 420Z" fill="#f0521a"/>
  <path d="M0 222 C300 74 450 54 600 54 C750 54 900 74 1200 222 L1200 420 L0 420Z" fill="#1f3f6e"/>
</svg>
<div class="abs" style="left:515px;top:4755px;width:170px;height:170px;border-radius:50%;background:#fff;display:flex;align-items:center;justify-content:center">
  <div style="width:56px;height:56px;border-radius:50%;background:var(--navy)"></div>
</div>
<footer class="footer">
  <div class="brand" style="top:5010px;color:#fff;font-size:30px"><span class="brand-dot" style="background:#fff;width:26px;height:26px"></span>Brightwell</div>
  <div class="social" style="left:140px">f</div>
  <div class="social" style="left:193px">in</div>

  <h4 style="left:341px;top:4938px">SiteMap</h4>
  <ul>
    <li style="left:341px;top:4980px">Home</li>
    <li style="left:341px;top:5009px">Services</li>
    <li style="left:341px;top:5038px">About Us</li>
    <li style="left:341px;top:5067px">Our People</li>
    <li style="left:341px;top:5096px">Safety &amp; Compliance</li>
    <li style="left:341px;top:5125px">Contact</li>
  </ul>

  <h4 style="left:599px;top:4938px">Contact Us</h4>
  <div class="info" style="left:598px;top:4990px"><svg width="18" height="22" viewBox="0 0 24 28"><path d="M12 2a9 9 0 0 0-9 9c0 7 9 15 9 15s9-8 9-15a9 9 0 0 0-9-9z" fill="none" stroke="#f0521a" stroke-width="2.4"/><circle cx="12" cy="11" r="3" fill="#f0521a"/></svg>Our Serving Area</div>
  <div class="info" style="left:598px;top:5042px"><svg width="18" height="18" viewBox="0 0 24 24"><path d="M6.6 10.8a15 15 0 0 0 6.6 6.6l2.2-2.2a1 1 0 0 1 1-.25 11.4 11.4 0 0 0 3.6.57 1 1 0 0 1 1 1V20a1 1 0 0 1-1 1A17 17 0 0 1 3 4a1 1 0 0 1 1-1h3.5a1 1 0 0 1 1 1c0 1.25.2 2.45.57 3.57a1 1 0 0 1-.25 1z" fill="#f0521a"/></svg>(07) 3900 5172</div>
  <div class="info" style="left:598px;top:5088px"><svg width="18" height="14" viewBox="0 0 24 18"><rect width="24" height="18" rx="2" fill="#f0521a"/><path d="M1 2l11 8 11-8" fill="none" stroke="#fff" stroke-width="2"/></svg>Email us</div>

  <h4 style="left:872px;top:4932px">Newsletter</h4>
  <p class="abs" style="left:872px;top:4970px;width:250px;font-size:13px;line-height:25px;color:#fff">Would you like to receive our exclusive update for signup !</p>
  <div class="abs" style="left:872px;top:5058px;width:251px;height:50px;border-radius:25px;background:#fff;font-size:13px;color:#777;line-height:50px;padding-left:20px">Enter Email *
    <div class="abs" style="right:4px;top:4px;width:42px;height:42px;border-radius:50%;background:var(--orange);display:flex;align-items:center;justify-content:center"><svg width="18" height="18" viewBox="0 0 24 24"><path d="M2 12l20-9-7 19-3-8z" fill="#fff"/></svg></div>
  </div>
</footer>
<div class="copyright">©Brightwell - 2020 All rights Reserved.</div>

</body>
</html>
```